Creative Design "Size Chart" for a Clothing Product

Hi, My dear friends! I am looking to do a contest to design a unique creative "Size Chart" for our clothing line. See Attached the Sizes & Ideas Thanks Good Luck Dorian

Colors

Designer to choose colors to be used in the design.

```html
<!DOCTYPE html>
<html lang="en">
<head>
<meta charset="utf-8">
<title>Women's Size Chart</title>
<link href="https://fonts.googleapis.com/css2?family=Jost:ital,wght@0,300;0,400;0,600;0,700;1,400&display=swap" rel="stylesheet">
<style>
  :root {
    --ink: #000000;
    --paper: #ffffff;
    --cell: #faf8f9;
    --garment-light: #f1f1f1;
    --garment-dark: #d9d9d9;
  }
  * { box-sizing: border-box; margin: 0; padding: 0; }
  html, body { width: 1200px; height: 1200px; overflow: hidden; background: var(--paper); }
  body { position: relative; font-family: "Jost", sans-serif; color: var(--ink); }

  .header {
    position: absolute; left: 84px; top: 38px; width: 1045px; height: 105px;
    border: 1.5px solid var(--ink);
  }
  .brand {
    position: absolute; left: 20px; top: 22px;
    font-family: "Jost", sans-serif; font-weight: 300; font-size: 50px; line-height: 1; letter-spacing: 1px;
  }
  .title {
    position: absolute; right: 42px; top: 26px;
    font-family: "Jost", sans-serif; font-weight: 700; font-size: 52px; line-height: 1; letter-spacing: 0.5px;
  }

  .garment {
    position: absolute; left: 392px; top: 194px; width: 382px; height: 470px;
    background: linear-gradient(180deg, var(--garment-light), var(--garment-dark));
    border-radius: 120px 120px 30px 30px / 60px 60px 20px 20px;
  }
  .measures { position: absolute; left: 0; top: 0; }
  .measure-label {
    position: absolute; left: 865px;
    font-family: "Jost", sans-serif; font-weight: 300; font-size: 28px; line-height: 1;
  }
  .measure-label.chest { top: 368px; }
  .measure-label.waist { top: 501px; }

  .size-table {
    position: absolute; left: 137px; top: 720px; width: 941px; height: 349px;
    border-collapse: collapse; table-layout: fixed;
  }
  .size-table td, .size-table th {
    border: 1px solid var(--ink); background: var(--cell);
    text-align: center; vertical-align: middle; height: 116px;
  }
  .size-table col.row-head { width: 215px; }
  .row-title { font-weight: 700; font-size: 34px; letter-spacing: -0.5px; }
  .unit { font-weight: 400; font-style: italic; font-size: 22px; }
  .size-code { display: block; font-weight: 700; font-size: 28px; line-height: 1.1; }
  .size-num { display: block; font-weight: 400; font-style: italic; font-size: 22px; line-height: 1.3; }
  .value { font-weight: 400; font-size: 28px; }
</style>
</head>
<body>
  <header class="header">
    <div class="brand">LOGO</div>
    <h1 class="title">WOMEN’S SIZE CHART</h1>
  </header>

  <div class="garment" role="img" aria-label="Fitted short-sleeve women's T-shirt shown on an invisible form"></div>

  <svg class="measures" width="1200" height="1200" viewBox="0 0 1200 1200" aria-hidden="true">
    <g fill="none" stroke="#000" stroke-width="1.2" stroke-dasharray="7 6">
      <path d="M421 370 Q412 380 440 388 Q560 400 680 382 Q705 376 700 370"/>
      <line x1="690" y1="386" x2="856" y2="386"/>
      <path d="M462 512 Q458 520 480 522 Q560 530 660 518 Q676 514 672 510"/>
      <line x1="668" y1="519" x2="846" y2="519"/>
    </g>
  </svg>
  <div class="measure-label chest">CHEST</div>
  <div class="measure-label waist">WAIST</div>

  <table class="size-table">
    <colgroup><col class="row-head"><col><col><col><col><col><col><col></colgroup>
    <tr>
      <th><span class="row-title">SIZE</span></th>
      <th><span class="size-code">XS</span><span class="size-num">0 - 2</span></th>
      <th><span class="size-code">S</span><span class="size-num">4 - 6</span></th>
      <th><span class="size-code">M</span><span class="size-num">8 - 10</span></th>
      <th><span class="size-code">L</span><span class="size-num">12 - 14</span></th>
      <th><span class="size-code">XL</span><span class="size-num">14 - 16</span></th>
      <th><span class="size-code">2X</span><span class="size-num">18</span></th>
      <th><span class="size-code">3X</span><span class="size-num">20</span></th>
    </tr>
    <tr>
      <th><span class="row-title">CHEST</span> <span class="unit">( cm )</span></th>
      <td class="value">32-34</td><td class="value">34-36</td><td class="value">36-38</td><td class="value">38-40</td><td class="value">40-42</td><td class="value">42-44</td><td class="value">44-46</td>
    </tr>
    <tr>
      <th><span class="row-title">WAIST</span> <span class="unit">( cm )</span></th>
      <td class="value">26-28</td><td class="value">28-30</td><td class="value">30-32</td><td class="value">32-34</td><td class="value">34-36</td><td class="value">36-38</td><td class="value">38-40</td>
    </tr>
  </table>
</body>
</html>
```